Need Exciting Podcast Cover Art Design for New Show!

We need a podcast art design for our new show. It is called "Spark Forge Climb a Label" and we've interviewed hundreds of proven online entrepreneurs and experts and asked them to share their best advice for starting an e-commerce product-based brand. I don't have a color palette however, I like Blue (but I'm open to your suggestion). I want a podcast cover art that stands out, jumps out when people are browsing.

Target Market(s)

People who have a product idea and want to sell it online directly to the consumer

Font styles to use
Sans Serif

Requirements
Must have
• It should have the name: The Spark Forge Climb a Label Show and the most important words in the title/they should stand out are Spark Forge Climb
Nice to have
• I want something simple yet I want it to pop out. For instance, if you use blue, add a hint of color to make it pop.

```html
<!DOCTYPE html>
<html lang="en">
<head>
<meta charset="utf-8">
<title>Spark Forge Climb – A Label Show</title>
<link rel="stylesheet" href="https://fonts.googleapis.com/css2?family=Oswald:wght@500&family=Open+Sans:wght@600;700&display=swap">
<style>
  :root {
    --stage: #3a3b3f;
    --paper: #ffffff;
    --mist: #f1f6fc;
    --sky: #0aa5ea;
    --art-top: #e4f0fb;
    --art-bottom: #fbe7b4;
    --gold: #fcc632;
    --gold-deep: #f5a516;
    --ink: #111111;
  }
  * { margin: 0; padding: 0; box-sizing: border-box; }
  html, body {
    width: 1200px; height: 1000px; overflow: hidden;
    background: var(--stage);
  }
  .cover {
    position: absolute; left: 236px; top: 120px;
    width: 728px; height: 728px;
    background: var(--paper);
    overflow: hidden;
  }
  .cover-backdrop { position: absolute; inset: 0; }
  .hero-illustration {
    position: absolute; left: 134px; top: 40px;
    width: 470px; height: 360px;
    border-radius: 24px;
    background: linear-gradient(180deg, var(--art-top) 0%, #eef5fc 55%, var(--art-bottom) 100%);
  }
  .show-title { color: var(--sky); font-weight: normal; }
  .title-lead, .title-key {
    position: absolute; left: 0; right: 0;
    text-align: center; white-space: nowrap;
  }
  .title-lead {
    top: 425px;
    font-family: "Oswald", "Arial Narrow", sans-serif;
    font-weight: 500; font-size: 84px; line-height: 84px;
  }
  .title-key {
    top: 498px;
    font-family: "Open Sans", Arial, sans-serif;
    font-weight: 700; font-size: 126px; line-height: 126px;
  }
  .show-tag {
    position: absolute; left: 169px; top: 622px;
    width: 390px; height: 63px;
    border-radius: 9px;
    background: linear-gradient(90deg, var(--gold-deep) 0 34px, var(--gold) 34px);
    display: flex; align-items: center; justify-content: center;
    font-family: "Open Sans", Arial, sans-serif;
    font-weight: 600; font-size: 30px; line-height: 1; color: var(--ink);
    letter-spacing: 0.5px;
  }
</style>
</head>
<body>
  <main class="cover">
    <svg class="cover-backdrop" width="728" height="728" viewBox="0 0 728 728" aria-hidden="true">
      <path d="M0 0 H300 C260 60 180 90 150 170 C120 240 60 230 0 235 Z" fill="var(--mist)"/>
      <path d="M440 0 H728 V240 C680 230 640 180 600 130 C560 80 480 60 440 0 Z" fill="var(--mist)"/>
      <path d="M0 560 C80 540 170 580 220 640 C260 690 300 728 300 728 H0 Z" fill="var(--mist)"/>
    </svg>
    <div class="hero-illustration" role="img" aria-label="Illustration of two business people shaking hands atop rising stacks of gold coins under an upward trend arrow, with two colleagues watching beside them"></div>
    <h1 class="show-title">
      <span class="title-lead">SPARK FORGE</span>
      <span class="title-key">CLIMB</span>
    </h1>
    <p class="show-tag">A LABEL SHOW</p>
  </main>
</body>
</html>
```